Webdesign for large cottage directory

We have developed a first version of a website that can accommodate large groups (10 to 300 people). The site is English and is aimed at a wide audience ranging from a group of students to a family or a family. For the visitors the site is free and it is the propietaires who pay to see their accommodation. The site is online with just a few fake lodgings and a simple design to the elements that must be appraised (nothing to keep the current design). Our website is here: 456abri.com (login / pass = admin / 123) Home page (456abri.com): on this page section) and lodging by theme (third section). These three points should be highlighted as possible. The displayed map may be slightly modified. Only the background and the color changes when hovering over the mouse. It can be enlarged / retreciated. Below these 3 sections we have some fairly published articles, the latest blog posts and the footer. The menu will be visible throughout the site. Category page (https://456abri.fr/gite-departement/aveyron OR https://456abri.fr/gites-couchages-121): On these pages we always return the same format with the googlemap, an image 1 text. Below the list of the cottages concerned and the filter options. Product page: The pages presenting the cottages can be of two types: - Either the cottage has no owner and there is no contact for the visitor to the owner that he can retrieve his cottage by registering: example of a page of this type: https://456abri.fr/domaine-de-varnoquet - The cottage to a propietaire and we are on the classic card. : // 456abri. en / domain-of-varnoquet2 For all products on the site we have nav tab. It's just for testing. We do not want to be in the design for real website. All information must be in the page without login / register page: classic, it's here: https://456abri.it/login and https://456abri.fr/register Blog homepage (https://456abri.fr/blog ): Classic blog page Blog post (https://456abri.fr/blog/urltemporaire1551521154) and static page (https://456abri.fr/blog/Systeme-classement-456abrifr): Nothing special Menu: Menu is an important part of the website. It's the way to navigate on the wbesite.
Number of Pages Required
4 page
Colors
Designer to choose colors to be used in the design.
Look and feel

```html
<!DOCTYPE html>
<html lang="fr">
<head>
<meta charset="utf-8">
<title>456abri – Gîtes pour grands groupes</title>
<link href="https://fonts.googleapis.com/css2?family=Montserrat:wght@400;500;600;700&family=Roboto:wght@400;500;700&display=swap" rel="stylesheet">
<style>
:root{
  --navy:#0d3564;
  --navy-dark:#0a2748;
  --blue:#1a5d9c;
  --orange:#f5a21b;
  --orange-dark:#e08a0c;
  --green:#19c39a;
  --lavender:#eef0fa;
  --ink:#1d2433;
  --muted:#6b7280;
  --line:#e3e6ee;
  --white:#ffffff;
}
*{box-sizing:border-box;margin:0;padding:0}
html,body{width:1200px;height:5158px;overflow:hidden}
body{font-family:"Montserrat",sans-serif;color:var(--ink);background:var(--white);position:relative}
.container{width:1020px;margin:0 auto;position:relative}
h2.section-title{font-family:"Roboto",sans-serif;font-weight:700;font-size:30px;color:var(--navy);display:flex;align-items:center;justify-content:center;gap:12px}
h2.section-title em{font-style:normal;color:var(--orange)}

/* header */
.site-header{height:130px;position:relative;background:var(--white)}
.brand-name{position:absolute;left:120px;top:44px;display:flex;align-items:center;gap:12px;font-family:"Montserrat",sans-serif;font-weight:500;font-size:32px;color:var(--ink)}
.brand-name .dot{width:16px;height:16px;background:var(--blue);border-radius:50%}
.topbar{position:absolute;right:0;top:0;height:48px;width:530px;background:var(--navy);clip-path:polygon(6% 0,100% 0,100% 100%,0 100%);display:flex;align-items:center;justify-content:flex-end;gap:28px;padding-right:40px;color:var(--white);font-size:15px;font-weight:500}
.topbar span{display:flex;align-items:center;gap:8px}
.topbar .socials{display:flex;gap:6px}
.topbar .socials i{width:22px;height:22px;border:2px solid var(--white);border-radius:50%;display:block}
.account{position:absolute;right:40px;top:78px;display:flex;gap:30px;font-size:13px;font-weight:600;color:var(--navy)}
.account span{display:flex;align-items:center;gap:7px}
.main-nav{height:42px;background:var(--navy);display:flex;align-items:center;padding-left:140px;gap:56px;font-size:15px;font-weight:600;color:var(--white)}
.main-nav .active{color:var(--orange)}

/* hero */
.hero{height:420px;position:relative;background:linear-gradient(160deg,#8a8f86 0%,#5b6158 45%,#3d433e 100%);text-align:center;color:var(--white)}
.hero-text{position:absolute;left:0;right:0;top:92px}
.hero-text p{font-size:31px;line-height:38px;font-weight:500;width:950px;margin:0 auto}
.hero-text h1{font-family:"Roboto",sans-serif;font-size:42px;font-weight:700;margin-top:6px}
.btn-start{display:inline-block;margin-top:44px;background:var(--orange-dark);color:var(--white);font-weight:700;font-size:20px;padding:16px 54px;border-radius:4px}
.hero-arrow{position:absolute;top:185px;width:40px;height:50px;background:rgba(255,255,255,.35);display:flex;align-items:center;justify-content:center}
.hero-arrow.prev{left:0}.hero-arrow.next{right:0}

/* capacities */
.capacities{height:457px;padding-top:90px}
.capacity-list{display:flex;justify-content:space-between;width:1000px;margin:70px auto 0}
.capacity{width:140px;text-align:center;font-size:20px;line-height:28px;color:var(--ink)}
.capacity svg{display:block;margin:0 auto 20px}

/* departements */
.departements{height:750px;background:var(--lavender);padding-top:88px}
.map{width:440px;height:515px;margin:60px auto 0;background:linear-gradient(180deg,#9aa6bd,#8795b0);border-radius:40% 35% 30% 45%/35% 40% 40% 35%}

/* themes */
.themes{height:1031px;background:linear-gradient(180deg,#1b4675 0%,#123a66 50%,#0d3058 100%);padding-top:92px}
.themes h2.section-title{color:var(--white)}
.theme-grid{display:grid;grid-template-columns:repeat(3,327px);column-gap:19px;row-gap:34px;width:1019px;margin:62px auto 0}
.theme figure{text-align:center}
.theme .photo{height:185px}
.theme figcaption{color:var(--white);font-size:17px;font-weight:500;margin-top:14px;text-align:center}

/* listings */
.listings{height:1160px;padding-top:86px;background:#fbfbfd}
.listing{height:306px;background:var(--white);border:1px solid var(--line);box-shadow:0 2px 10px rgba(13,53,100,.08);position:relative;margin-bottom:40px}
.listing .photo{position:absolute;left:14px;top:14px;width:300px;height:210px}
.listing h3{position:absolute;left:340px;top:18px;font-size:19px;font-weight:700;color:var(--ink)}
.amenities{position:absolute;right:24px;top:14px;display:flex;gap:18px}
.facts{position:absolute;left:340px;top:70px;width:650px;display:grid;grid-template-columns:300px 200px 150px;row-gap:20px;font-size:13px;line-height:17px;color:var(--muted)}
.fact{display:flex;gap:10px}
.fact .ico{width:34px;height:34px;flex:none;border-radius:6px;background:#e6e8ef}
.fact b{display:block;color:var(--ink);font-weight:600;font-size:14px}
.listing-foot{position:absolute;left:0;right:0;bottom:0;height:70px;border-top:1px solid var(--line);display:flex;align-items:center}
.desc-tab{height:70px;width:160px;background:var(--green);color:var(--white);font-weight:600;font-size:15px;display:flex;align-items:center;padding-left:22px;clip-path:polygon(0 0,78% 0,100% 100%,0 100%)}
.listing-foot p{flex:1;font-size:14px;line-height:20px;color:var(--blue);padding:0 20px}
.btn-fav{align-self:flex-end;height:38px;margin-right:14px;margin-bottom:10px;background:var(--blue);color:var(--white);font-size:14px;font-weight:600;display:flex;align-items:center;gap:8px;padding:0 18px}

/* blog */
.blog{height:687px;padding-top:120px}
.blog-grid{display:grid;grid-template-columns:repeat(3,327px);column-gap:19px;margin-top:42px}
.post .photo{height:183px}
.post .date{display:flex;align-items:center;gap:10px;margin-top:18px;font-size:15px;color:var(--ink)}
.post p{font-size:16px;line-height:22px;margin-top:14px;color:var(--ink)}
.post a{display:block;margin-top:16px;font-size:15px;color:var(--blue);text-decoration:none}

/* footer */
.site-footer{height:440px;background:linear-gradient(180deg,#163a63,#0b2544);color:var(--white);padding-top:84px}
.footer-brand{display:flex;align-items:center;justify-content:center;gap:12px;font-weight:500;font-size:32px}
.footer-brand .dot{width:16px;height:16px;background:var(--white);border-radius:50%}
.footer-cols{display:grid;grid-template-columns:220px 230px 230px 300px;width:1000px;margin:52px auto 0;font-size:13px;font-weight:600}
.footer-cols h4{font-size:14px;font-weight:700;letter-spacing:.5px;margin-bottom:20px}
.footer-cols li{list-style:none;line-height:20px}
.contact-line{display:flex;gap:10px;margin-bottom:14px;line-height:17px}
.contact-line i,.follow i{width:22px;height:22px;border:2px solid var(--white);border-radius:50%;flex:none;display:block}
.follow{display:flex;align-items:center;gap:10px;margin-bottom:16px}
.newsletter p{font-size:12px;line-height:17px;font-weight:500}
.email-field{margin-top:14px;width:250px;height:32px;border-radius:16px;background:var(--white);color:var(--muted);font-size:12px;display:flex;align-items:center;padding-left:16px}
.btn-sub{margin-top:12px;display:inline-block;background:var(--blue);padding:8px 22px;font-size:12px;font-weight:700}
.copyright{height:41px;background:var(--orange);color:var(--white);font-size:13px;font-weight:600;display:flex;align-items:center;justify-content:center;letter-spacing:.4px}
</style>
</head>
<body>

<header class="site-header">
  <div class="brand-name"><span class="dot"></span>456abri</div>
  <div class="topbar">
    <span><svg width="16" height="16" viewBox="0 0 16 16"><path d="M3 1h3l1 4-2 1a9 9 0 0 0 5 5l1-2 4 1v3a2 2 0 0 1-2 2A13 13 0 0 1 1 3a2 2 0 0 1 2-2z" fill="#fff"/></svg>1800.987.6543</span>
    <span><svg width="18" height="14" viewBox="0 0 18 14"><rect x="1" y="1" width="16" height="12" fill="none" stroke="#fff" stroke-width="2"/><path d="M1 1l8 7 8-7" fill="none" stroke="#fff" stroke-width="2"/></svg>info@456abri.fr</span>
    <div class="socials"><i></i><i></i><i></i></div>
  </div>
  <div class="account">
    <span><svg width="16" height="16" viewBox="0 0 16 16"><circle cx="8" cy="5" r="4" fill="#0d3564"/><path d="M0 16a8 7 0 0 1 16 0z" fill="#0d3564"/></svg>Register</span>
    <span><svg width="14" height="16" viewBox="0 0 14 16"><rect x="0" y="7" width="14" height="9" rx="1" fill="#0d3564"/><path d="M3 7V5a4 4 0 0 1 8 0v2" fill="none" stroke="#0d3564" stroke-width="2"/></svg>Login</span>
    <span><svg width="16" height="16" viewBox="0 0 16 16"><circle cx="8" cy="8" r="7" fill="#1a5d9c"/></svg>EN ▾</span>
  </div>
</header>

<nav class="main-nav">
  <span class="active">Home</span>
  <span>Gite par capacité ▾</span>
  <span>Gite par département ▾</span>
  <span>Gite par thématique ▾</span>
  <span>Blog</span>
  <span>Contactez nous</span>
</nav>

<section class="hero" role="img" aria-label="Photo d'un grand gîte en pierre entouré d'arbres">
  <div class="hero-arrow prev"><svg width="14" height="22" viewBox="0 0 14 22"><path d="M12 2L3 11l9 9" fill="none" stroke="#fff" stroke-width="3"/></svg></div>
  <div class="hero-arrow next"><svg width="14" height="22" viewBox="0 0 14 22"><path d="M2 2l9 9-9 9" fill="none" stroke="#fff" stroke-width="3"/></svg></div>
  <div class="hero-text">
    <p>Vous cherchez un endroit pour faire la fête? Ou cherchez-vous un lieu pour une réunion de famille ou un mariage?</p>
    <h1>Nous avons une solution pour vous</h1>
    <span class="btn-start">Commencer</span>
  </div>
</section>

<section class="capacities">
  <h2 class="section-title"><svg width="30" height="24" viewBox="0 0 30 24"><circle cx="9" cy="6" r="5" fill="#0d3564"/><circle cx="21" cy="6" r="5" fill="#0d3564"/><path d="M0 24a9 9 0 0 1 18 0zM12 24a9 9 0 0 1 18 0z" fill="#0d3564"/></svg>Gîtes par <em>capacités</em></h2>
  <div class="capacity-list">
    <div class="capacity"><svg width="112" height="112" viewBox="0 0 112 112"><circle cx="56" cy="56" r="50" fill="none" stroke="#f5a21b" stroke-width="7" stroke-dasharray="3 7"/><circle cx="56" cy="36" r="8" fill="#f5a21b"/><path d="M44 56a12 10 0 0 1 24 0z" fill="#f5a21b"/><text x="56" y="76" text-anchor="middle" font-family="Montserrat,sans-serif" font-size="13" font-weight="700" fill="#f5a21b">2 à 20</text></svg>2 à 20<br>personnes</div>
    <div class="capacity"><svg width="112" height="112" viewBox="0 0 112 112"><circle cx="56" cy="56" r="50" fill="none" stroke="#1a5d9c" stroke-width="7" stroke-dasharray="3 7"/><circle cx="56" cy="36" r="8" fill="#1a5d9c"/><path d="M44 56a12 10 0 0 1 24 0z" fill="#1a5d9c"/><text x="56" y="76" text-anchor="middle" font-family="Montserrat,sans-serif" font-size="13" font-weight="700" fill="#1a5d9c">20 à 40</text></svg>20 à 40<br>personnes</div>
    <div class="capacity"><svg width="112" height="112" viewBox="0 0 112 112"><circle cx="56" cy="56" r="50" fill="none" stroke="#f5a21b" stroke-width="7" stroke-dasharray="3 7"/><circle cx="56" cy="36" r="8" fill="#f5a21b"/><path d="M44 56a12 10 0 0 1 24 0z" fill="#f5a21b"/><text x="56" y="76" text-anchor="middle" font-family="Montserrat,sans-serif" font-size="13" font-weight="700" fill="#f5a21b">40 à 60</text></svg>40 à 60<br>personnes</div>
    <div class="capacity"><svg width="112" height="112" viewBox="0 0 112 112"><circle cx="56" cy="56" r="50" fill="none" stroke="#1a5d9c" stroke-width="7" stroke-dasharray="3 7"/><circle cx="56" cy="36" r="8" fill="#1a5d9c"/><path d="M44 56a12 10 0 0 1 24 0z" fill="#1a5d9c"/><text x="56" y="76" text-anchor="middle" font-family="Montserrat,sans-serif" font-size="13" font-weight="700" fill="#1a5d9c">60 à 80</text></svg>60 à 80<br>personnes</div>
    <div class="capacity"><svg width="112" height="112" viewBox="0 0 112 112"><circle cx="56" cy="56" r="50" fill="none" stroke="#f5a21b" stroke-width="7" stroke-dasharray="3 7"/><circle cx="56" cy="36" r="8" fill="#f5a21b"/><path d="M44 56a12 10 0 0 1 24 0z" fill="#f5a21b"/><text x="56" y="76" text-anchor="middle" font-family="Montserrat,sans-serif" font-size="13" font-weight="700" fill="#f5a21b">80 à 120</text></svg>80 à 120<br>personnes</div>
    <div class="capacity"><svg width="112" height="112" viewBox="0 0 112 112"><circle cx="56" cy="56" r="50" fill="none" stroke="#1a5d9c" stroke-width="7" stroke-dasharray="3 7"/><circle cx="56" cy="36" r="8" fill="#1a5d9c"/><path d="M44 56a12 10 0 0 1 24 0z" fill="#1a5d9c"/><text x="56" y="76" text-anchor="middle" font-family="Montserrat,sans-serif" font-size="13" font-weight="700" fill="#1a5d9c">+de 120</text></svg>+de 120<br>personnes</div>
  </div>
</section>

<section class="departements">
  <h2 class="section-title"><svg width="30" height="30" viewBox="0 0 30 30"><rect x="2" y="4" width="26" height="22" rx="2" fill="none" stroke="#0d3564" stroke-width="3"/><path d="M15 8a5 5 0 0 1 5 5c0 4-5 9-5 9s-5-5-5-9a5 5 0 0 1 5-5z" fill="#0d3564"/></svg>Gîtes par <em>departement</em></h2>
  <div class="map" role="img" aria-label="Carte interactive des départements de France"></div>
</section>

<section class="themes">
  <h2 class="section-title"><svg width="30" height="28" viewBox="0 0 30 28"><rect x="1" y="8" width="20" height="18" rx="2" fill="#fff"/><rect x="9" y="1" width="20" height="18" rx="2" fill="none" stroke="#fff" stroke-width="2.5"/></svg>Gîtes par <em>thématique</em></h2>
  <div class="theme-grid">
    <figure class="theme"><div class="photo" role="img" aria-label="Photo d'une salle de séminaire" style="background:linear-gradient(135deg,#2b2b2f,#6a6258)"></div><figcaption>Seminaire</figcaption></figure>
    <figure class="theme"><div class="photo" role="img" aria-label="Photo d'une barque sur un lac au coucher du soleil" style="background:linear-gradient(180deg,#7d5fa6,#d97a8a 55%,#4b3a6e)"></div><figcaption>Pêche?</figcaption></figure>
    <figure class="theme"><div class="photo" role="img" aria-label="Photo d'une moto tout-terrain dans les herbes" style="background:linear-gradient(135deg,#c89a4e,#7a5a2e)"></div><figcaption>Moto classe transplantée</figcaption></figure>
    <figure class="theme"><div class="photo" role="img" aria-label="Photo de fonds marins turquoise" style="background:linear-gradient(180deg,#2a8fa3,#0e4d66)"></div><figcaption>Aquatique</figcaption></figure>
    <figure class="theme"><div class="photo" role="img" aria-label="Silhouette d'un cavalier au coucher du soleil" style="background:linear-gradient(180deg,#f2a93b,#c9661d 60%,#3a230e)"></div><figcaption>Equitation</figcaption></figure>
    <figure class="theme"><div class="photo" role="img" aria-label="Photo d'une montagne enneigée avec randonneurs" style="background:linear-gradient(180deg,#9fb4cf,#e9eef4)"></div><figcaption>Neige nature et randonnée</figcaption></figure>
    <figure class="theme"><div class="photo" role="img" aria-label="Photo d'un paysage vallonné pour le VTT" style="background:linear-gradient(180deg,#8fb0d2,#6f8a4a 55%,#a0783e)"></div><figcaption>VTT</figcaption></figure>
    <figure class="theme"><div class="photo" role="img" aria-label="Photo d'une salle de restaurant" style="background:linear-gradient(135deg,#3d2a1c,#b07a3e)"></div><figcaption>Gastronomique</figcaption></figure>
    <figure class="theme"><div class="photo" role="img" aria-label="Photo d'une plage de colonie de vacances" style="background:linear-gradient(180deg,#c9dfe9,#e6e4dc)"></div><figcaption>Colonie de vacances</figcaption></figure>
  </div>
</section>

<section class="listings">
  <div class="container">
    <article class="listing">
      <div class="photo" role="img" aria-label="Photo d'un chalet en bois sous la neige" style="background:linear-gradient(135deg,#c9ccd2,#6e4f3a)"></div>
      <h3>Domaine de varnoquet</h3>
      <div class="amenities">
        <svg width="22" height="26" viewBox="0 0 22 26"><circle cx="6" cy="4" r="3" fill="#f5a21b"/><circle cx="16" cy="4" r="3" fill="#f5a21b"/><rect x="2" y="9" width="8" height="17" rx="2" fill="#f5a21b"/><rect x="12" y="9" width="8" height="17" rx="2" fill="#f5a21b"/></svg>
        <svg width="26" height="26" viewBox="0 0 26 26"><path d="M2 24l10-10M6 6l14 14M24 2l-8 8" stroke="#f5a21b" stroke-width="3"/></svg>
        <svg width="28" height="22" viewBox="0 0 28 22"><path d="M2 18a12 12 0 0 1 24 0z" fill="#f5a21b"/><rect x="0" y="19" width="28" height="3" fill="#f5a21b"/></svg>
        <svg width="26" height="22" viewBox="0 0 26 22"><path d="M1 8a17 17 0 0 1 24 0M5 12a11 11 0 0 1 16 0M9 16a5 5 0 0 1 8 0" fill="none" stroke="#f5a21b" stroke-width="3"/><circle cx="13" cy="20" r="2" fill="#f5a21b"/></svg>
        <svg width="24" height="26" viewBox="0 0 24 26"><circle cx="10" cy="3" r="3" fill="#f5a21b"/><path d="M10 7v8h8l3 8M6 12a8 8 0 1 0 10 10" fill="none" stroke="#f5a21b" stroke-width="3"/></svg>
      </div>
      <div class="facts">
        <div class="fact"><span class="ico"></span><div><b>Address</b>27 Rue des Tilleuls<br>75011 Paris, France</div></div>
        <div class="fact"><span class="ico"></span><div><b>Région</b>Occitanie</div></div>
        <div class="fact"><span class="ico"></span><div><b>Departement</b>Aveyron</div></div>
        <div class="fact"><span class="ico"></span><div><b>Capacité</b>600</div></div>
        <div class="fact" style="grid-column:span 2"><span class="ico"></span><div><b>Formule proposée</b>Gestion libre, Pension complete, Nuitée seule</div></div>
      </div>
      <div class="listing-foot">
        <span class="desc-tab">Description</span>
        <p>Qu'est-ce que le Lorem Ipsum? Le Lorem Ipsum est simplement du faux texte employé dans la composition et la mise en page avant impression.</p>
        <span class="btn-fav"><svg width="16" height="16" viewBox="0 0 16 16"><path d="M8 1l2.2 4.6 5 .6-3.7 3.4 1 5L8 12.2 3.5 14.6l1-5L.8 6.2l5-.6z" fill="none" stroke="#fff" stroke-width="1.5"/></svg>Ajouter aux favoris</span>
      </div>
    </article>

    <article class="listing">
      <div class="photo" role="img" aria-label="Photo d'une grande maison bourgeoise avec jardin" style="background:linear-gradient(135deg,#7a8a6a,#4d5a44 60%,#a7a59a)"></div>
      <h3>Domaine de paris</h3>
      <div class="amenities">
        <svg width="22" height="26" viewBox="0 0 22 26"><circle cx="6" cy="4" r="3" fill="#f5a21b"/><circle cx="16" cy="4" r="3" fill="#f5a21b"/><rect x="2" y="9" width="8" height="17" rx="2" fill="#f5a21b"/><rect x="12" y="9" width="8" height="17" rx="2" fill="#f5a21b"/></svg>
        <svg width="26" height="26" viewBox="0 0 26 26"><path d="M2 24l10-10M6 6l14 14M24 2l-8 8" stroke="#f5a21b" stroke-width="3"/></svg>
        <svg width="28" height="22" viewBox="0 0 28 22"><path d="M2 18a12 12 0 0 1 24 0z" fill="#f5a21b"/><rect x="0" y="19" width="28" height="3" fill="#f5a21b"/></svg>
        <svg width="26" height="22" viewBox="0 0 26 22"><path d="M1 8a17 17 0 0 1 24 0M5 12a11 11 0 0 1 16 0M9 16a5 5 0 0 1 8 0" fill="none" stroke="#f5a21b" stroke-width="3"/><circle cx="13" cy="20" r="2" fill="#f5a21b"/></svg>
        <svg width="24" height="26" viewBox="0 0 24 26"><circle cx="10" cy="3" r="3" fill="#f5a21b"/><path d="M10 7v8h8l3 8M6 12a8 8 0 1 0 10 10" fill="none" stroke="#f5a21b" stroke-width="3"/></svg>
      </div>
      <div class="facts">
        <div class="fact"><span class="ico"></span><div><b>Address</b>27 Rue des Tilleuls<br>75011 Paris, France</div></div>
        <div class="fact"><span class="ico"></span><div><b>Région</b>Occitanie</div></div>
        <div class="fact"><span class="ico"></span><div><b>Departement</b>Aveyron</div></div>
        <div class="fact"><span class="ico"></span><div><b>Capacité</b>600</div></div>
        <div class="fact" style="grid-column:span 2"><span class="ico"></span><div><b>Formule proposée</b>Gestion libre, Pension complete, Nuitée seule</div></div>
      </div>
      <div class="listing-foot">
        <span class="desc-tab">Description</span>
        <p>Qu'est-ce que le Lorem Ipsum? Le Lorem Ipsum est simplement du faux texte employé dans la composition et la mise en page avant impression.</p>
        <span class="btn-fav"><svg width="16" height="16" viewBox="0 0 16 16"><path d="M8 1l2.2 4.6 5 .6-3.7 3.4 1 5L8 12.2 3.5 14.6l1-5L.8 6.2l5-.6z" fill="none" stroke="#fff" stroke-width="1.5"/></svg>Ajouter aux favoris</span>
      </div>
    </article>

    <article class="listing">
      <div class="photo" role="img" aria-label="Photo d'une façade ancienne avec balcon" style="background:linear-gradient(135deg,#d8d2c6,#8c8070)"></div>
      <h3>Domaine de gaule</h3>
      <div class="amenities">
        <svg width="22" height="26" viewBox="0 0 22 26"><circle cx="6" cy="4" r="3" fill="#f5a21b"/><circle cx="16" cy="4" r="3" fill="#f5a21b"/><rect x="2" y="9" width="8" height="17" rx="2" fill="#f5a21b"/><rect x="12" y="9" width="8" height="17" rx="2" fill="#f5a21b"/></svg>
        <svg width="26" height="26" viewBox="0 0 26 26"><path d="M2 24l10-10M6 6l14 14M24 2l-8 8" stroke="#f5a21b" stroke-width="3"/></svg>
        <svg width="28" height="22" viewBox="0 0 28 22"><path d="M2 18a12 12 0 0 1 24 0z" fill="#f5a21b"/><rect x="0" y="19" width="28" height="3" fill="#f5a21b"/></svg>
        <svg width="26" height="22" viewBox="0 0 26 22"><path d="M1 8a17 17 0 0 1 24 0M5 12a11 11 0 0 1 16 0M9 16a5 5 0 0 1 8 0" fill="none" stroke="#f5a21b" stroke-width="3"/><circle cx="13" cy="20" r="2" fill="#f5a21b"/></svg>
        <svg width="24" height="26" viewBox="0 0 24 26"><circle cx="10" cy="3" r="3" fill="#f5a21b"/><path d="M10 7v8h8l3 8M6 12a8 8 0 1 0 10 10" fill="none" stroke="#f5a21b" stroke-width="3"/></svg>
      </div>
      <div class="facts">
        <div class="fact"><span class="ico"></span><div><b>Address</b>27 Rue des Tilleuls<br>75011 Paris, France</div></div>
        <div class="fact"><span class="ico"></span><div><b>Région</b>Occitanie</div></div>
        <div class="fact"><span class="ico"></span><div><b>Departement</b>Aveyron</div></div>
        <div class="fact"><span class="ico"></span><div><b>Capacité</b>600</div></div>
        <div class="fact" style="grid-column:span 2"><span class="ico"></span><div><b>Formule proposée</b>Gestion libre, Pension complete, Nuitée seule</div></div>
      </div>
      <div class="listing-foot">
        <span class="desc-tab">Description</span>
        <p>Qu'est-ce que le Lorem Ipsum? Le Lorem Ipsum est simplement du faux texte employé dans la composition et la mise en page avant impression.</p>
        <span class="btn-fav"><svg width="16" height="16" viewBox="0 0 16 16"><path d="M8 1l2.2 4.6 5 .6-3.7 3.4 1 5L8 12.2 3.5 14.6l1-5L.8 6.2l5-.6z" fill="none" stroke="#fff" stroke-width="1.5"/></svg>Ajouter aux favoris</span>
      </div>
    </article>
  </div>
</section>

<section class="blog">
  <div class="container">
    <h2 class="section-title"><svg width="28" height="30" viewBox="0 0 28 30"><rect x="2" y="2" width="20" height="26" rx="2" fill="none" stroke="#0d3564" stroke-width="3"/><path d="M7 9h10M7 15h10M7 21h6" stroke="#0d3564" stroke-width="2.5"/></svg>Blog</h2>
    <div class="blog-grid">
      <article class="post">
        <div class="photo" role="img" aria-label="Photo d'une rue de ville ancienne" style="background:linear-gradient(180deg,#b9c9dc,#b59a7a 60%,#6e5a48)"></div>
        <div class="date"><svg width="18" height="18" viewBox="0 0 18 18"><rect x="1" y="3" width="16" height="14" rx="1" fill="none" stroke="#0d3564" stroke-width="2"/><path d="M1 7h16M5 1v4M13 1v4" stroke="#0d3564" stroke-width="2"/></svg>Jan 14, 2019</div>
        <p>Duis aute irure dolor in reprehen Lorem ipsum dolor sit amet, cons ectetur adipiscing elit, sed do eius mod tempor incididunt.</p>
        <a>Read more...</a>
      </article>
      <article class="post">
        <div class="photo" role="img" aria-label="Photo d'un village de montagne enneigé" style="background:linear-gradient(180deg,#3f6aa0,#dfe6ee 55%,#7a5440)"></div>
        <div class="date"><svg width="18" height="18" viewBox="0 0 18 18"><rect x="1" y="3" width="16" height="14" rx="1" fill="none" stroke="#0d3564" stroke-width="2"/><path d="M1 7h16M5 1v4M13 1v4" stroke="#0d3564" stroke-width="2"/></svg>Jan 14, 2019</div>
        <p>Duis aute irure dolor in reprehen Lorem ipsum dolor sit amet, cons ectetur adipiscing elit, sed do eius mod tempor incididunt.</p>
        <a>Read more...</a>
      </article>
      <article class="post">
        <div class="photo" role="img" aria-label="Photo d'une maison sous la neige" style="background:linear-gradient(180deg,#c7d3e0,#e8ecef 60%,#8a6b55)"></div>
        <div class="date"><svg width="18" height="18" viewBox="0 0 18 18"><rect x="1" y="3" width="16" height="14" rx="1" fill="none" stroke="#0d3564" stroke-width="2"/><path d="M1 7h16M5 1v4M13 1v4" stroke="#0d3564" stroke-width="2"/></svg>Jan 14, 2019</div>
        <p>Duis aute irure dolor in reprehen Lorem ipsum dolor sit amet, cons ectetur adipiscing elit, sed do eius mod tempor incididunt.</p>
        <a>Read more...</a>
      </article>
    </div>
  </div>
</section>

<footer class="site-footer">
  <div class="footer-brand"><span class="dot"></span>456abri</div>
  <div class="footer-cols">
    <div>
      <h4>QUICK LINKS</h4>
      <ul><li>Gite par capacité</li><li>Gite par departement</li><li>Gite par thematique</li><li>Blog</li><li>Contactez nous</li></ul>
    </div>
    <div>
      <h4>CONTACT</h4>
      <div class="contact-line"><i></i><span>27 Rue des Tilleuls<br>75011 Paris, France</span></div>
      <div class="contact-line"><i></i><span>1800.987.6543</span></div>
      <div class="contact-line"><i></i><span>info@456abri.fr</span></div>
    </div>
    <div>
      <h4>FOLLOW US</h4>
      <div class="follow"><i></i>Fil social</div>
      <div class="follow"><i></i>Fil court</div>
      <div class="follow"><i></i>Fil photo</div>
    </div>
    <div class="newsletter">
      <h4>NEWSLETTER</h4>
      <p>Register your email address to get news information about us and our services</p>
      <div class="email-field">Email Address</div>
      <span class="btn-sub">SUBSCRIBE</span>
    </div>
  </div>
</footer>
<div class="copyright">COPYRIGHT © 2019 456ABRI. ALL RIGHTS RESERVED</div>

</body>
</html>
```